Website of QUORVEX | The Amber Frontier Company

I need a simple and effective website where users can quickly understand what the company is all about and the added value of the services provided. The site should be attractive and modern, based on the logo and on the corporate slideshow attached.

Target Market(s)

Public and Private organizations from maritime security and defense, looking for solutions in the field s of digital transformation and cybersecurity.

Coding

Coded - Design and coding required

Requirements
Must have
• A form through which can contact the company by email to request additional information.

```html
<!DOCTYPE html>
<html lang="en">
<head>
<meta charset="utf-8">
<title>QUORVEX | The Amber Frontier Company</title>
<link rel="stylesheet" href="https://fonts.googleapis.com/css2?family=Poppins:ital,wght@0,300;0,400;0,500;0,600;1,400;1,500;1,600&display=swap">
<style>
:root{
  --blue:#1e8ad6;
  --blue-soft:#5bb6e8;
  --navy:#0c2a48;
  --ink:#111a24;
  --text:#2b2f36;
  --sky:#e7f4fc;
  --mist:#f1f1f1;
  --white:#ffffff;
  --line:#2f95dc;
}
*{box-sizing:border-box;margin:0;padding:0}
html,body{width:1200px;height:5059px;overflow:hidden}
body{position:relative;font-family:'Poppins',sans-serif;color:var(--text);background:var(--white)}
.abs{position:absolute}
.backdrop{position:absolute;left:0;top:0}
.mark{display:inline-block;background:var(--blue);border-radius:8px}
.btn{position:absolute;display:flex;align-items:center;justify-content:center;background:var(--blue);color:var(--white);font-weight:500;border-radius:14px 0 14px 0;box-shadow:4px 4px 0 var(--navy);text-decoration:none}

/* header */
.brand{position:absolute;display:flex;align-items:center;gap:12px}
.brand-name{font-weight:600;color:var(--ink);line-height:1;letter-spacing:1px}
.brand-tag{font-size:8px;letter-spacing:3px;color:var(--ink);font-weight:500;margin-top:4px}
.nav a{position:absolute;top:62px;font-size:12px;color:var(--ink);text-decoration:none;font-weight:500}
.nav a.active{color:var(--blue)}

/* hero */
.hero-card{left:130px;top:206px;width:514px;height:395px;background:rgba(255,255,255,.4);border-radius:28px;text-align:center}
.hero-card h1{margin-top:70px;font-size:36px;line-height:41px;font-weight:500;color:var(--ink)}
.hero-card p{margin-top:12px;font-size:14px;font-style:italic;line-height:18px;color:var(--ink)}

/* section heading */
.sec-head{position:absolute;display:flex;align-items:center;gap:16px}
.sec-head .mark{width:66px;height:68px;border-radius:10px}
.sec-head h2{font-size:37px;font-weight:500;line-height:1;color:var(--ink)}
.sec-head small{display:block;font-size:11px;letter-spacing:3px;font-weight:500;margin-top:8px;color:var(--ink)}

.about-copy{left:155px;top:935px;width:430px;font-size:14.5px;line-height:25px;text-align:justify;color:var(--ink)}
.about-copy p+p{margin-top:12px}
.arch{border:3px solid var(--line);border-radius:210px 210px 0 0;overflow:hidden}
.arch div{width:100%;height:100%}

/* services */
.card{top:1595px;width:432px;height:540px;text-align:center}
.card .ring{position:absolute;left:138px;top:56px;width:156px;height:156px;border-radius:50%;border:2px dotted currentColor}
.card h3{position:absolute;top:258px;width:100%;font-size:26px;font-weight:600}
.card p{position:absolute;top:312px;width:100%;padding:0 48px;font-size:17px;line-height:33px}
.card a{position:absolute;top:440px;left:0;width:100%;font-size:23px;font-weight:600;text-decoration:underline;text-underline-offset:5px;color:inherit}
.card-strategy{left:143px;background:linear-gradient(160deg,#7cc8f1,#4fa9e0);color:var(--white)}
.card-delivery{left:625px;background:linear-gradient(160deg,#e4e6e8,#f3f3f3);color:var(--ink)}
.card-delivery h3{color:var(--blue)}

/* why choose */
.hub{left:424px;top:2583px;width:334px;height:334px;border-radius:50%;background:var(--white);box-shadow:0 0 0 10px #f3f5f7,0 4px 18px rgba(0,0,0,.12)}
.feat-icon{width:124px;height:124px;border-radius:50%}
.feat-icon.dark{background:#111}
.feat-icon.blue{background:var(--blue)}
.feat-icon::after{content:"";position:absolute;inset:12px;border-radius:50%;border:2px dotted rgba(255,255,255,.8)}
.feat{font-size:10.5px;line-height:17px;color:var(--ink);width:190px}
.feat b{display:block;font-weight:600;font-size:11.5px;margin-bottom:4px}
.feat.right{text-align:right}

/* collaborate */
.collab-title{left:0;width:1200px;top:3338px;text-align:center;font-size:44px;font-style:italic;font-weight:500;color:var(--white)}
.collab-copy{left:0;width:1200px;top:3424px;text-align:center;font-size:17px;line-height:28px;color:var(--white)}

/* contact form */
.intro{left:69px;top:4008px;font-size:14px;color:var(--ink)}
.field{position:absolute;background:var(--white);border:1px solid #dde3e8;font-size:12px;color:#b7bec6;padding:12px 14px}

/* footer */
.foot-h{font-size:22px;font-weight:500;color:var(--ink)}
.links li{position:absolute;list-style:none;font-size:14px;color:var(--ink)}
.links li::before{content:"";position:absolute;left:-20px;top:6px;width:7px;height:7px;border-radius:50%;background:var(--blue)}
.social{width:36px;height:36px;border-radius:50%;background:var(--blue)}
.cicon{width:34px;height:34px;border-radius:50%;background:var(--blue)}
.cline{font-size:14px;color:var(--ink);line-height:24px}
.rule{left:69px;top:4988px;width:1064px;height:1px;background:var(--line)}
.copy{left:0;width:1200px;top:5014px;text-align:center;font-size:13px;color:var(--ink)}
</style>
</head>
<body>

<svg class="backdrop" width="1200" height="5059" viewBox="0 0 1200 5059">
  <defs>
    <linearGradient id="sea" x1="0" y1="0" x2="1" y2="1">
      <stop offset="0" stop-color="#0b6f8d"/><stop offset=".6" stop-color="#1a9cb5"/><stop offset="1" stop-color="#0e6e8c"/>
    </linearGradient>
    <linearGradient id="deep" x1="0" y1="0" x2="1" y2="1">
      <stop offset="0" stop-color="#0a2846"/><stop offset=".55" stop-color="#164f7d"/><stop offset="1" stop-color="#0d3558"/>
    </linearGradient>
    <linearGradient id="team" x1="0" y1="0" x2="0" y2="1">
      <stop offset="0" stop-color="#e3f1fb"/><stop offset=".5" stop-color="#cfe4f3"/><stop offset="1" stop-color="#bcd8ee"/>
    </linearGradient>
  </defs>
  <rect x="0" y="141" width="1200" height="4480" fill="var(--sky)"/>
  <path d="M0,1180 C220,1320 420,1330 620,1285 C820,1240 1010,1250 1200,1310 V2260 H0 Z" fill="var(--mist)"/>
  <path role="img" aria-label="Team working together at laptops, faded behind the section" d="M0,2170 C200,2240 420,2290 640,2250 C860,2210 1020,2250 1200,2290 V3100 H0 Z" fill="url(#team)"/>
  <path role="img" aria-label="Aerial photo of a cargo ship sailing across deep blue sea" d="M0,2960 C200,3080 400,3090 600,3040 C800,2990 1000,2990 1200,3060 V3620 C1000,3560 800,3620 600,3700 C400,3780 200,3760 0,3730 Z" fill="url(#deep)"/>
  <path role="img" aria-label="Aerial photo of a container ship on turquoise water" d="M0,141 H1200 V766 C1100,700 1000,560 850,600 C650,650 450,700 250,660 C120,630 40,600 0,580 Z" fill="url(#sea)"/>
  <path d="M0,4480 C250,4560 500,4610 760,4570 C980,4535 1100,4540 1200,4560 V5059 H0 Z" fill="var(--white)"/>
</svg>

<!-- header -->
<div class="brand" style="left:69px;top:58px">
  <span class="mark" style="width:34px;height:36px"></span>
  <div><div class="brand-name" style="font-size:24px">QUORVEX</div><div class="brand-tag">AMBER FRONTIER</div></div>
</div>
<nav class="nav">
  <a class="active" style="left:415px" href="#">HOME</a>
  <a style="left:483px" href="#">ABOUT US</a>
  <a style="left:576px" href="#">OUR SERVICES</a>
  <a style="left:701px" href="#">WHY CHOOSE US</a>
  <a style="left:845px" href="#">TESTIMONIALS</a>
</nav>
<a class="btn" style="left:980px;top:45px;width:151px;height:50px;font-size:17px" href="#">Contact Us</a>

<!-- hero -->
<div class="abs hero-card">
  <h1>INNOVATIVE SOLUTIONS<br>FOR MARITIME SECURITY<br>AND DEFENSE</h1>
  <p>Empowering Organizations with Cutting-Edge<br>Consulting and Technology</p>
</div>
<a class="btn" style="left:287px;top:475px;width:150px;height:44px;font-size:15px" href="#">Know More</a>

<!-- about -->
<div class="sec-head" style="left:155px;top:831px">
  <span class="mark"></span>
  <div><h2>ABOUT US</h2><small>WHO WE ARE</small></div>
</div>
<div class="abs about-copy">
  <p><b>QUORVEX</b> specializes in delivering innovative solutions for maritime security and defense in the fields of digital transformation and cybersecurity.</p>
  <p>By combining unparalleled expertise with strategic partnerships, we empower organizations to overcome challenges, seize opportunities, and achieve success.</p>
</div>
<a class="btn" style="left:155px;top:1119px;width:112px;height:32px;font-size:13px" href="#">Read More</a>
<div class="abs arch" style="left:656px;top:770px;width:406px;height:454px">
  <div role="img" aria-label="Photo of four business professionals standing in an office" style="background:linear-gradient(180deg,#eef1f4,#c9d3de 55%,#7c8ea3)"></div>
</div>

<!-- services -->
<div class="sec-head" style="left:405px;top:1457px">
  <span class="mark"></span>
  <div><h2>OUR SERVICES</h2><small>WHAT WE DO</small></div>
</div>
<div class="abs card card-strategy" role="img" aria-label="Blue-tinted photo of colleagues planning together">
  <span class="ring"></span>
  <h3>STRATEGY AND DESIGN</h3>
  <p>Services focused on helping clients define their vision, assess their needs, and design innovative solutions.</p>
  <a href="#">READ MORE</a>
</div>
<div class="abs card card-delivery" role="img" aria-label="Faded photo of a hand writing with a pen">
  <span class="ring"></span>
  <h3>EXECUTION AND DELIVERY</h3>
  <p>Services focused on turning strategies into reality by driving implementation, integration, and operational success.</p>
  <a href="#">READ MORE</a>
</div>

<!-- why choose us -->
<div class="sec-head" style="left:405px;top:2406px">
  <span class="mark"></span>
  <div><h2>WHY CHOOSE US</h2><small>QUORVEX</small></div>
</div>
<div class="abs hub"></div>
<div class="brand" style="left:466px;top:2726px">
  <span class="mark" style="width:44px;height:48px"></span>
  <div><div class="brand-name" style="font-size:34px">QUORVEX</div><div class="brand-tag" style="font-size:10px">AMBER FRONTIER</div></div>
</div>

<div class="abs feat-icon dark" style="left:280px;top:2580px"></div>
<div class="abs feat right" style="left:71px;top:2612px"><b>INNOVATIVE SOLUTIONS</b>Leveraging cutting-edge tech-nology and strategic insights.</div>
<div class="abs feat-icon blue" style="left:280px;top:2811px"></div>
<div class="abs feat right" style="left:71px;top:2846px"><b>TAILORED STRATEGIES</b>Customized designs addressing unique organizational needs.</div>
<div class="abs feat-icon blue" style="left:784px;top:2580px"></div>
<div class="abs feat" style="left:927px;top:2568px;width:190px"><b>EXPERT TEAM</b>Decades of combined worldwide experience in maritime security, defense, digital transformation, and cybersecurity, in public, private and research organizations, and in multinational and multidisciplinary teams.</div>
<div class="abs feat-icon dark" style="left:784px;top:2811px"></div>
<div class="abs feat" style="left:927px;top:2836px;width:190px"><b>PROVEN PARTNERSHIPS</b>Access to state-of-the-art knowledge, practices and technology through key alliances.</div>

<!-- collaborate -->
<div class="sec-head" style="left:357px;top:3235px">
  <span class="mark"></span>
  <div><h2 style="color:var(--white)">LET'S COLLABORATE</h2><small style="color:var(--white)">QUORVEX</small></div>
</div>
<div class="abs collab-title">READY TO INNOVATE TOGETHER?</div>
<div class="abs collab-copy">QUORVEX is here to help you navigate challenges and unlock new opportunities for maritime security<br>and defense with digital transformation and cybersecurity solutions.</div>
<a class="btn" style="left:521px;top:3507px;width:155px;height:46px;font-size:15px" href="#">Know More</a>

<!-- contact -->
<div class="sec-head" style="left:69px;top:3899px">
  <span class="mark"></span>
  <div><h2>CONTACT US</h2><small>GET IN TOUCH</small></div>
</div>
<div class="abs intro">For more information,Please fill out the following and we will be in touch shortly.</div>
<form>
  <div class="field" style="left:71px;top:4062px;width:267px;height:46px">First Name</div>
  <div class="field" style="left:365px;top:4062px;width:267px;height:46px">Last Name</div>
  <div class="field" style="left:71px;top:4134px;width:267px;height:46px">Phone</div>
  <div class="field" style="left:365px;top:4134px;width:267px;height:46px">Email</div>
  <div class="field" style="left:71px;top:4203px;width:561px;height:161px">Message</div>
</form>
<a class="btn" style="left:73px;top:4395px;width:112px;height:34px;font-size:14px" href="#">Submit</a>
<div class="abs arch" style="left:707px;top:3928px;width:406px;height:452px">
  <div role="img" aria-label="Photo of a businesswoman checking her phone at a desk" style="background:linear-gradient(180deg,#f4f1ec,#d9d3ca 50%,#a9a49c)"></div>
</div>

<!-- footer -->
<div class="brand" style="left:157px;top:4784px">
  <span class="mark" style="width:46px;height:48px"></span>
  <div><div class="brand-name" style="font-size:34px">QUORVEX</div><div class="brand-tag" style="font-size:10px">AMBER FRONTIER</div></div>
</div>
<span class="abs social" style="left:214px;top:4872px"></span>
<span class="abs social" style="left:261px;top:4872px"></span>
<span class="abs social" style="left:308px;top:4872px"></span>

<div class="abs foot-h" style="left:534px;top:4722px">LINKS</div>
<ul class="links">
  <li style="left:558px;top:4800px">Home</li>
  <li style="left:558px;top:4831px">About Us</li>
  <li style="left:558px;top:4863px">Services</li>
  <li style="left:558px;top:4896px">Why Choose Us</li>
  <li style="left:558px;top:4928px">Contact Us</li>
</ul>

<div class="abs foot-h" style="left:795px;top:4722px">CONTACT US</div>
<svg class="abs cicon" style="left:794px;top:4795px" viewBox="0 0 34 34"><path d="M17 8a6 6 0 0 0-6 6c0 5 6 12 6 12s6-7 6-12a6 6 0 0 0-6-6zm0 8.5a2.5 2.5 0 1 1 0-5 2.5 2.5 0 0 1 0 5z" fill="#fff"/></svg>
<div class="abs cline" style="left:845px;top:4797px">465, Lorem Ipsum<br>Lorem Ipsum , Lorem Ipsum</div>
<svg class="abs cicon" style="left:794px;top:4858px" viewBox="0 0 34 34"><path d="M12 9l3 0 2 5-2 1.5c1 2.2 2.5 3.7 4.5 4.5L21 18l5 2v3c0 1-1 2-2 2C16 25 9 18 9 11c0-1 1-2 3-2z" fill="#fff"/></svg>
<div class="abs cline" style="left:845px;top:4863px">+1 555 014 2290</div>
<svg class="abs cicon" style="left:794px;top:4911px" viewBox="0 0 34 34"><rect x="9" y="11" width="16" height="12" rx="1.5" fill="#fff"/><path d="M9.5 12l7.5 6 7.5-6" stroke="#1e8ad6" stroke-width="1.6" fill="none"/></svg>
<div class="abs cline" style="left:845px;top:4916px">office@quorvex.com</div>

<div class="abs rule"></div>
<div class="abs copy">Copyright © 2025 All Rights Reserved By Company Name</div>

</body>
</html>
```